Halcyon Bus Card

i own a building in the bronx ny - its called "Halcyon 7 by 2 HDFC"i want a classy logo / business card - nothing too religuous but it is like a family there - its a large apartment building - colors i like dark red, black, medium shade of gray also reg business card stuff tel # 845-555-0172 address 3862 Larkmoor Ave Bronx NY 10471 Email fijosh@aol.comslogan - " Together under one roof "i can send u a picture of the building for the backside

```html
<!DOCTYPE html>
<html lang="en">
<head>
<meta charset="utf-8">
<title>Halcyon 7 by 2 HDFC – Business Card</title>
<link href="https://fonts.googleapis.com/css2?family=Source+Sans+3:wght@400;600;700&display=swap" rel="stylesheet">
<style>
  :root {
    --backdrop: #95bec1;
    --card-white: #f3f2ef;
    --brand-red: #b3151b;
    --deep-red: #8e1216;
    --bright-red: #c8201f;
    --ink: #1b1b1b;
    --gray: #555555;
    --white: #ffffff;
  }
  * { box-sizing: border-box; margin: 0; padding: 0; }
  html, body {
    width: 1200px; height: 960px; overflow: hidden;
    background: var(--backdrop);
    font-family: "Source Sans 3", sans-serif;
  }
  .card-sheet {
    width: 1200px; height: 960px;
    display: flex; flex-direction: column;
    align-items: center; justify-content: center; gap: 56px;
  }
  .card {
    position: relative;
    width: 640px; height: 366px;
    overflow: hidden;
    box-shadow: 0 8px 22px rgba(0,0,0,0.18);
  }

  /* Front */
  .card-front { background: var(--card-white); }
  .brand-lockup {
    position: absolute; top: 48px; left: 0; right: 0;
    display: flex; flex-direction: column; align-items: center;
  }
  .brand-row { display: flex; align-items: center; gap: 12px; }
  .brand-dot {
    width: 22px; height: 22px; border-radius: 50%;
    background: var(--brand-red);
    flex: none;
  }
  .brand-name {
    font-weight: 700; font-size: 28px; letter-spacing: 0.5px; line-height: 1.1;
    color: var(--brand-red); text-transform: uppercase;
  }
  .brand-slogan {
    margin-top: 6px;
    font-size: 12px; letter-spacing: 2px; color: var(--gray);
    text-transform: uppercase;
  }
  .holder {
    position: absolute; top: 152px; left: 0; right: 0; text-align: center;
  }
  .holder-name {
    font-weight: 700; font-size: 26px; color: var(--ink); letter-spacing: 0.3px; line-height: 1.15;
  }
  .holder-position {
    font-size: 17px; color: var(--brand-red); letter-spacing: 0.5px; line-height: 1.3;
  }
  .contact-row {
    position: absolute; top: 230px; left: 0; right: 0;
    display: flex; justify-content: center; gap: 26px;
    font-size: 20px; line-height: 1.2; color: var(--ink);
  }
  .contact-item { display: flex; align-items: center; gap: 10px; white-space: nowrap; }
  .icon-badge {
    width: 22px; height: 22px; border-radius: 50%;
    background: var(--brand-red);
    display: flex; align-items: center; justify-content: center;
    flex: none;
  }
  .address-band {
    position: absolute; left: 0; right: 0; top: 286px; height: 52px;
    background: var(--brand-red);
    display: flex; align-items: center; justify-content: center; gap: 12px;
    color: var(--white); font-size: 20px; letter-spacing: 0.3px; white-space: nowrap;
  }

  /* Back */
  .card-back {
    background: radial-gradient(circle at 62% 70%, var(--bright-red) 0%, var(--brand-red) 45%, var(--deep-red) 100%);
  }
  .skyline-art {
    position: absolute; left: 0; top: 40px; width: 330px; height: 326px;
    background: linear-gradient(180deg, rgba(255,255,255,0.10) 0%, rgba(255,255,255,0.05) 100%);
  }
  .back-brand {
    position: absolute; right: 36px; bottom: 44px;
    display: flex; align-items: center; gap: 12px;
  }
  .back-brand .brand-dot { background: var(--white); }
  .back-brand .brand-name { color: var(--white); font-size: 28px; }
</style>
</head>
<body>
<main class="card-sheet">

  <section class="card card-front" aria-label="Business card front">
    <div class="brand-lockup">
      <div class="brand-row">
        <span class="brand-dot"></span>
        <span class="brand-name">Halcyon 7 by 2 HDFC</span>
      </div>
      <p class="brand-slogan">Together under one roof</p>
    </div>

    <div class="holder">
      <p class="holder-name">YOUR NAME</p>
      <p class="holder-position">POSITION</p>
    </div>

    <div class="contact-row">
      <span class="contact-item">
        <span class="icon-badge">
          <svg width="12" height="12" viewBox="0 0 24 24"><path fill="#fff" d="M6.6 10.8a15.1 15.1 0 0 0 6.6 6.6l2.2-2.2a1 1 0 0 1 1-.25 11.4 11.4 0 0 0 3.6.57 1 1 0 0 1 1 1V20a1 1 0 0 1-1 1A17 17 0 0 1 3 4a1 1 0 0 1 1-1h3.5a1 1 0 0 1 1 1c0 1.25.2 2.45.57 3.57a1 1 0 0 1-.25 1z"/></svg>
        </span>
        845-555-0172
      </span>
      <span class="contact-item">
        <span class="icon-badge">
          <svg width="13" height="10" viewBox="0 0 26 20"><rect x="1.5" y="1.5" width="23" height="17" fill="none" stroke="#fff" stroke-width="2.4"/><path d="M2 2l11 9 11-9" fill="none" stroke="#fff" stroke-width="2.4"/></svg>
        </span>
        kelmar@mailbrook.net
      </span>
    </div>

    <div class="address-band">
      <svg width="14" height="20" viewBox="0 0 14 20"><path fill="#fff" d="M7 0a7 7 0 0 0-7 7c0 5 7 13 7 13s7-8 7-13a7 7 0 0 0-7-7zm0 9.6A2.6 2.6 0 1 1 7 4.4a2.6 2.6 0 0 1 0 5.2z"/></svg>
      <span>3862 Larkmoor Ave, Bronx NY 10471</span>
    </div>
  </section>

  <section class="card card-back" aria-label="Business card back">
    <div class="skyline-art" role="img" aria-label="Faint illustration of apartment towers"></div>
    <div class="back-brand">
      <span class="brand-dot"></span>
      <span class="brand-name">Halcyon</span>
    </div>
  </section>

</main>
</body>
</html>
```